"1" Pager Webdesign + HTML Creation

In this project we ask you to create a 1 pager (the registration form will be opened on a second page) web design with the content & structure described in the attached PDF. You are absolutely free in your choice of colors & design. There is also no company logo on this site as it will serve as a demo site for future clients where the design & content can be adjusted.
Once we agree on the design we also ask you to convert it into a simple html page.
The site is not a regular company website with services etc. --> the main idea is to give client the ability to launch a dedicated server (VPS) fully automatically in the background from the web gui. This server will have a software installed that allows phishing simulations to test employees security awareness.....so there should be some logical flow from top to bottom that leads to the user to launch the server. The company details/ressources etc. are not important and can be really kept very small. Main point of the site is to explain user what the steps he needs to go through to launch that virtual server...so launch button must be also kinda big...
See example I created (jpg) --> I am not designer. This is just to illustrate what I mean with logical "flow"....
As for pricing: I don't expect a fully functional html site & finished design for this price and I am willing to pay an extra bonus for finalizing the design/site as I know the details are time consuming. This bonus could be agreed upon project start and paid via zenvora. What I want are a few design examples that show that you understood what I need. Depending how much custom graphics need to be created we can discuss extra bonus/time required...
The site is not a regular company website with services etc. --> the main idea is to give client the ability to launch a dedicated server (VPS) fully automatically in the background from the web gui. This server will have a software installed that allows phishing simulations to test employees security awareness.....so there should be some logical flow from top to bottom that leads to the user to launch the server.... Added Thursday, August 11, 2016
Coding
Coded - Design and coding required
Number of Pages Required
2 page
Look and feel

```html
<!DOCTYPE html>
<html lang="en">
<head>
<meta charset="utf-8">
<title>Baitwise GmbH – Start to Phish</title>
<link href="https://fonts.googleapis.com/css2?family=Oswald:wght@400;500&family=Open+Sans:wght@400;600&display=swap" rel="stylesheet">
<style>
:root{
  --red:#e8433a;
  --red-dark:#d2362d;
  --yellow:#f7c325;
  --ink:#2d2d2d;
  --charcoal:#2b2b2b;
  --grey-text:#555;
  --light:#f0f0f0;
  --white:#fff;
}
*{box-sizing:border-box;margin:0;padding:0}
html,body{width:1200px;height:3689px;overflow:hidden}
body{font-family:"Open Sans",Arial,sans-serif;color:var(--ink);background:var(--white)}
.display{font-family:"Oswald",Arial,sans-serif;font-weight:400;text-transform:uppercase;line-height:1.1}
section,header,footer{position:relative;width:1200px;overflow:hidden}

/* nav */
.topbar{height:81px;background:var(--red);display:flex;align-items:center;justify-content:space-between;padding:0 60px 0 133px}
.brand{font-family:"Oswald",sans-serif;font-size:34px;color:var(--white);font-weight:400}
.menu{display:flex;gap:36px;list-style:none;font-size:13px;color:var(--white)}
.menu .active{text-decoration:underline}

/* hero */
.hero{height:553px;background:radial-gradient(circle at 50% 40%,#4a4a4c,#2e2e30 75%);color:var(--white);text-align:center}
.hero .intro{font-size:38px;padding-top:30px}
.hero .headline{font-size:62px;color:var(--yellow);margin-top:6px}
.hero .tagline{font-family:"Oswald",sans-serif;font-size:32px;margin-top:6px}
.hero p{font-size:15px;line-height:1.6;margin-top:10px}
.btn-outline{display:inline-block;border:1px solid #bbb;padding:10px 28px;font-size:15px;margin-top:18px;color:var(--white)}
.hero-media{width:400px;height:230px;margin:22px auto 0;background:linear-gradient(#d8dce3,#9aa3b1);border:14px solid #1d1d1d;border-bottom-width:22px;border-radius:8px 8px 2px 2px}

/* defense */
.defense{height:434px;text-align:center}
.defense .pre{font-family:"Oswald",sans-serif;font-size:32px;padding-top:42px}
.defense .big{font-size:62px;color:var(--red);margin-top:4px}
.defense .post{font-family:"Oswald",sans-serif;font-size:32px;margin-top:2px}
.pillars{display:flex;justify-content:center;gap:60px;margin-top:26px}
.pillar{width:420px}
.pillar svg{width:64px;height:64px}
.pillar h3{font-family:"Oswald",sans-serif;font-weight:400;font-size:32px;margin-top:8px}
.pillar p{font-size:13px;line-height:1.4;color:var(--grey-text)}

/* how */
.how{height:402px;background:var(--red);color:var(--white);text-align:center}
.how h2{font-size:62px;padding-top:50px}
.how .sub{font-size:15px;margin-top:10px}
.phases{display:flex;justify-content:center;margin-top:26px}
.phase{width:330px;position:relative;padding:0 14px}
.divider{flex:none;width:20px;height:110px}
.phase .num{position:absolute;left:8px;top:0;font-family:"Oswald",sans-serif;font-size:70px;line-height:1;color:rgba(255,255,255,.35)}
.phase .head{padding:0 0 0 50px;height:74px}
.phase svg{width:28px;height:28px}
.phase h3{font-family:"Oswald",sans-serif;font-weight:400;font-size:25px;line-height:1.3}
.phase .lead{font-size:14px;line-height:1.4}
.phase ul{list-style:none;font-size:11px;line-height:1.7;margin-top:6px;opacity:.9}
.phase .small{font-size:11px;margin-top:6px;opacity:.9;line-height:1.5}

/* steps */
.steps{height:590px;background:var(--red-dark);color:var(--white)}
.notch{position:absolute;left:825px;top:0}
.step{position:absolute;left:133px;display:flex;gap:22px}
.step .icon{width:62px;height:62px;background:var(--white);display:flex;align-items:center;justify-content:center;flex:none}
.step .icon svg{width:26px;height:26px}
.step h4{font-family:"Oswald",sans-serif;font-weight:400;font-size:21px;margin-top:-4px}
.step p{font-size:14px;line-height:1.45;width:920px}
.connector{position:absolute;left:163px;width:2px;background:var(--white)}
.connector::after{content:"";position:absolute;left:-6px;bottom:-2px;border:7px solid transparent;border-top:9px solid var(--white);border-bottom:0}

/* start */
.start{height:431px;text-align:center}
.start svg{margin-top:46px}
.start h2{font-size:62px;color:var(--red);margin-top:14px}
.form-box{position:absolute;left:133px;top:204px;width:932px;height:212px;background:var(--red);padding:20px 30px}
.row{display:flex;gap:20px}
.field{flex:1;height:37px;background:var(--white);font-size:12px;color:#555;padding:10px;text-align:left;display:flex;justify-content:space-between}
.area{height:74px;margin-top:12px;flex:none;width:100%;align-items:flex-start}
.btn-solid{display:inline-block;background:var(--white);color:var(--red);border:1px solid #fff;font-size:15px;padding:9px 22px;margin-top:14px;font-weight:600}

/* resources */
.resources{height:571px;background:var(--charcoal);color:var(--white);text-align:center}
.resources h2{font-size:62px;padding-top:42px}
.res-cols{display:flex;justify-content:center;gap:66px;margin-top:22px}
.res{width:401px}
.res h3{font-family:"Open Sans",sans-serif;font-weight:400;font-size:24px}
.res p{font-size:12px;line-height:1.45;color:#bbb;margin-top:8px}
.btn-red{display:inline-block;background:var(--red);color:var(--white);font-size:14px;padding:9px 20px;margin-top:16px}
.thumb{height:205px;margin-top:20px;background:linear-gradient(135deg,#5a5f68,#2a2e35);display:flex;align-items:center;justify-content:center}

/* about */
.about{height:245px;text-align:center}
.about h2{font-size:62px;color:var(--red);padding-top:36px}
.about p{width:1000px;margin:12px auto 0;font-size:14px;line-height:1.55;color:var(--grey-text)}

/* contact */
.contact{height:239px;display:flex;background:var(--light)}
.map{width:607px;height:239px;background:linear-gradient(135deg,#e4e4e4,#cfd2d4)}
.ask{padding:22px 0 0 40px}
.ask h3{font-family:"Oswald",sans-serif;font-weight:400;font-size:26px}
.ask h3 span{font-family:"Open Sans",sans-serif;font-size:12px}
.ask .grid{display:grid;grid-template-columns:170px 182px;gap:10px 25px;margin-top:8px}
.ask .field{height:39px;border:1px solid #ddd}
.submit{background:var(--charcoal);color:var(--white);font-size:13px;display:flex;align-items:center;justify-content:center;height:39px}

/* footer */
.footer{height:143px;background:var(--charcoal);color:#ddd;font-size:12px;text-align:center}
.info{display:flex;gap:56px;padding:26px 0 0 133px;align-items:center;white-space:nowrap}
.info span{display:flex;gap:8px;align-items:center}
.socials{margin-left:auto;margin-right:120px;display:flex;gap:20px}
.socials i{display:block;width:10px;height:10px;border-radius:50%;background:#999}
.footnav{margin-top:28px}
.copy{margin-top:8px;font-size:11px;color:#999}
</style>
</head>
<body>

<header class="topbar">
  <div class="brand">Baitwise GmbH</div>
  <ul class="menu">
    <li class="active">Home</li><li>Intro</li><li>How it works</li><li>Resources</li><li>About Us</li>
  </ul>
</header>

<section class="hero">
  <div class="intro display">{Intro} in 10 minutes from</div>
  <div class="headline display">Start to Phish!</div>
  <div class="tagline">People = Endpoints</div>
  <p>Raising your Security Posture means securing the people.<br>Isn't it time that we invest in our people as seriously as we invest in technology?</p>
  <div class="btn-outline">Watch the video and learn more</div>
  <div class="hero-media" role="img" aria-label="Laptop showing the intro video with a play button"></div>
</section>

<section class="defense">
  <div class="pre">Build Your Best</div>
  <div class="big display">Human Phishing and Malware Defense</div>
  <div class="post">with us</div>
  <div class="pillars">
    <div class="pillar">
      <svg viewBox="0 0 64 64"><path d="M6 8v50h52" fill="none" stroke="#2d2d2d" stroke-width="4"/><rect x="16" y="30" width="7" height="22" fill="#2d2d2d"/><rect x="28" y="20" width="7" height="32" fill="#2d2d2d"/><rect x="40" y="26" width="7" height="26" fill="#2d2d2d"/><rect x="52" y="14" width="5" height="38" fill="#2d2d2d"/></svg>
      <h3>Train Your Users</h3>
      <p>Choose among many ondemand interactive, engaging training modules<br>(customizable tips, video's, games, quiz etc.)</p>
    </div>
    <div class="pillar">
      <svg viewBox="0 0 64 64"><path d="M10 54l26-26" stroke="#2d2d2d" stroke-width="8" stroke-linecap="round"/><circle cx="44" cy="20" r="12" fill="#2d2d2d"/><circle cx="50" cy="14" r="6" fill="#fff"/></svg>
      <h3>Test Your Users</h3>
      <p>Fully automated Spear Phishing, Malware, Smishing, &amp; USB attack<br>Simulations</p>
    </div>
  </div>
</section>

<section class="how">
  <h2 class="display">How does it work?</h2>
  <div class="sub">It's so easy. After registration you can launch a virtualized server with a full scale testing and education platform within minutes.</div>
  <div class="phases">
    <div class="phase">
      <span class="num">1</span>
      <div class="head">
        <svg viewBox="0 0 32 32"><circle cx="16" cy="16" r="13" fill="none" stroke="#fff" stroke-width="3"/><path d="M10 16l4 4 8-8" fill="none" stroke="#fff" stroke-width="3"/></svg>
        <h3>Basic Settings</h3>
      </div>
      <div class="lead">Choose your preferred campaign settings</div>
      <ul><li>• Duration of campaign (up to 3 years)</li><li>• Number of employees to test/train</li><li>• Technical Details (domain names etc.)</li><li>• Choose additional services (Campaign Setup Support etc.)</li></ul>
    </div>
    <svg class="divider" viewBox="0 0 20 110"><polyline points="2,0 18,55 2,110" fill="none" stroke="rgba(255,255,255,.55)" stroke-width="1.5"/></svg>
    <div class="phase">
      <span class="num">2</span>
      <div class="head">
        <svg viewBox="0 0 32 32"><path d="M4 16h16M14 9l7 7-7 7" fill="none" stroke="#fff" stroke-width="3"/><path d="M18 4h10v24H18" fill="none" stroke="#fff" stroke-width="3"/></svg>
        <h3>Access</h3>
      </div>
      <div class="lead">Access your training platform</div>
      <div class="small">We will automatically launch a virtualized server<br>and send you the login credentials* via mail.</div>
    </div>
    <svg class="divider" viewBox="0 0 20 110"><polyline points="2,0 18,55 2,110" fill="none" stroke="rgba(255,255,255,.55)" stroke-width="1.5"/></svg>
    <div class="phase">
      <span class="num">3</span>
      <div class="head">
        <svg viewBox="0 0 32 32"><g stroke="#fff" stroke-width="3"><path d="M3 8h26M3 16h26M3 24h26"/></g><g fill="#fff"><rect x="8" y="4" width="5" height="8"/><rect x="19" y="12" width="5" height="8"/><rect x="11" y="20" width="5" height="8"/></g></svg>
        <h3>Web Wizard</h3>
      </div>
      <div class="lead">Configure your training &amp; phishing campaign</div>
      <div class="small">Use our simple, intuitive web based configuration wizard to finish your campaign</div>
    </div>
  </div>
</section>

<section class="steps">
  <svg class="notch" width="170" height="50" viewBox="0 0 170 50"><polygon points="0,0 170,0 85,50" fill="#e8433a"/></svg>

  <div class="step" style="top:50px">
    <div class="icon"><svg viewBox="0 0 26 26" fill="#d2362d"><rect x="2" y="4" width="5" height="4"/><rect x="9" y="4" width="15" height="4"/><rect x="2" y="11" width="5" height="4"/><rect x="9" y="11" width="15" height="4"/><rect x="2" y="18" width="5" height="4"/><rect x="9" y="18" width="15" height="4"/></svg></div>
    <div><h4>Step 1 : Campaign Selection</h4><p>Select your campaign type (e.g. training only, training combined with phishing simulation etc.). Choose among a huge selection of phishing &amp; Training templates to create your basic configuration</p></div>
  </div>
  <div class="connector" style="top:116px;height:48px"></div>

  <div class="step" style="top:170px">
    <div class="icon"><svg viewBox="0 0 26 26"><circle cx="13" cy="13" r="10" fill="none" stroke="#d2362d" stroke-width="2"/><circle cx="13" cy="13" r="4" fill="#d2362d"/></svg></div>
    <div><h4>Step 2 : Define the target</h4><p>Import your mail addresses (or phone numbers)</p></div>
  </div>
  <div class="connector" style="top:236px;height:48px"></div>

  <div class="step" style="top:290px">
    <div class="icon"><svg viewBox="0 0 26 26"><rect x="2" y="5" width="22" height="16" fill="#d2362d"/><path d="M2 5l11 9 11-9" fill="none" stroke="#fff" stroke-width="2"/></svg></div>
    <div><h4>Step 3 : Choose mail template</h4><p>Choose a Message template and customize the content or design tailored to your needs</p></div>
  </div>
  <div class="connector" style="top:356px;height:48px"></div>

  <div class="step" style="top:410px">
    <div class="icon"><svg viewBox="0 0 26 26"><rect x="2" y="4" width="22" height="14" fill="none" stroke="#d2362d" stroke-width="2.5"/><path d="M9 23h8M13 18v5" stroke="#d2362d" stroke-width="2.5"/></svg></div>
    <div><h4>Step 4 : Choose web landing page</h4><p>With more than 100 existing phishing &amp; malware templates you can pick a real live phishing or malware scenario that matches your company's risk</p></div>
  </div>
  <div class="connector" style="top:476px;height:40px"></div>

  <div class="step" style="top:516px">
    <div class="icon"><svg viewBox="0 0 26 26"><path d="M24 2L2 11l9 4 4 9z" fill="#d2362d"/></svg></div>
    <div><h4>Step 5 : Start!</h4><p>Start your campaign &amp; monitor the results in real time</p></div>
  </div>
</section>

<section class="start">
  <svg width="60" height="60" viewBox="0 0 60 60"><path d="M56 4C40 4 26 12 18 28l14 14c16-8 24-22 24-38z" fill="#e8433a"/><path d="M18 28l-12 2 8-12 10-2zM32 42l-2 12 12-8 2-10z" fill="#e8433a"/><path d="M14 40c-6 2-8 10-8 14 4 0 12-2 14-8z" fill="#e8433a"/><circle cx="42" cy="18" r="5" fill="#fff"/></svg>
  <h2 class="display">Get Started</h2>
  <div class="form-box">
    <div class="row">
      <div class="field">Name</div><div class="field">Email</div><div class="field">Phone</div><div class="field">Service for <span>▾</span></div>
    </div>
    <div class="field area">Message</div>
    <div class="btn-solid">Start Now</div>
  </div>
</section>

<section class="resources">
  <h2 class="display">Ressources</h2>
  <div class="res-cols">
    <div class="res">
      <h3>Service</h3>
      <p>Pellentesque habitant morbi tristique senectus et netus et malesuada fames ac turpis egestas. Fusce lorem elit, tincidunt eget pellentesque at, suscipit et lectus. Nulla et diam lacus.</p>
      <div class="btn-red">⤓ Download</div>
      <div class="thumb" role="img" aria-label="Video still of a laptop showing a malware alert">
        <svg width="64" height="64" viewBox="0 0 64 64"><circle cx="32" cy="32" r="28" fill="none" stroke="#fff" stroke-width="4"/><path d="M26 20l18 12-18 12z" fill="#fff"/></svg>
      </div>
    </div>
    <div class="res">
      <h3>About Us</h3>
      <p>Pellentesque habitant morbi tristique senectus et netus et malesuada fames ac turpis egestas. Fusce lorem elit, tincidunt eget pellentesque at, suscipit et lectus. Nulla et diam lacus.</p>
      <div class="btn-red">⤓ Download</div>
      <div class="thumb" role="img" aria-label="Video still of a security analyst at a dark workstation">
        <svg width="64" height="64" viewBox="0 0 64 64"><circle cx="32" cy="32" r="28" fill="none" stroke="#fff" stroke-width="4"/><path d="M26 20l18 12-18 12z" fill="#fff"/></svg>
      </div>
    </div>
  </div>
</section>

<section class="about">
  <h2 class="display">About Us</h2>
  <p>We launched this service because we saw a real opportunity in leveraging the everyday employee in the fight against phishing. After all, it's the employee being targeted. Our Security Education Platform includes integrated knowledge assessments, a library of simulated attacks, and interactive training modules, which have been proven to reduce successful phishing attacks and malware infections by up to 90%. Together with our partner Norvak GmbH we ensure that we always keep up with latest attack trends.</p>
</section>

<section class="contact">
  <div class="map" role="img" aria-label="Street map of the office location"></div>
  <div class="ask">
    <h3>Question? <span>Please get in contact with us</span></h3>
    <div class="grid">
      <div class="field">Name</div><div class="field">Email</div>
      <div class="field">Phone</div><div class="field">Category <span>▾</span></div>
      <div class="field">Message</div><div class="submit">SUBMIT</div>
    </div>
  </div>
</section>

<footer class="footer">
  <div class="info">
    <span><svg width="12" height="16" viewBox="0 0 12 16"><path d="M6 0a6 6 0 0 0-6 6c0 4 6 10 6 10s6-6 6-10a6 6 0 0 0-6-6z" fill="#ddd"/><circle cx="6" cy="6" r="2" fill="#2b2b2b"/></svg>24 Building name, Street name, City - Zipcode</span>
    <span><svg width="14" height="14" viewBox="0 0 14 14"><path d="M3 0l3 3-2 2c1 2 3 4 5 5l2-2 3 3-2 3C6 14 0 8 0 3z" fill="#ddd"/></svg>Call Now : 555 204 7719</span>
    <span><svg width="14" height="10" viewBox="0 0 14 10"><rect width="14" height="10" fill="#ddd"/><path d="M0 0l7 6 7-6" fill="none" stroke="#2b2b2b"/></svg>Email : hello@baitwise-demo.com</span>
    <div class="socials"><i></i><i></i><i></i><i></i></div>
  </div>
  <div class="footnav">Home &nbsp;|&nbsp; Intro &nbsp;|&nbsp; How it works &nbsp;|&nbsp; Resources &nbsp;|&nbsp; About Us</div>
  <div class="copy">Copyright © 2016 Baitwise GmbH. All rights reserved.</div>
</footer>

</body>
</html>
```